Tavrento - Staffing APP for the hospitality industry.

I need 7 screens designed that form the core of the APP. Tavrento is a staffing APP for the hospitality industry where workers sign up and complete details about themselves and their qualifications and experience. They also switch a button ON and OFF showing their availability status. Venues/employers then scan for workers based on job type, availability, distance etc

Industry/Entity Type

Hospitality employment industry

Number of Pages Required

5+ page

Requirements
Must have
• Refer wire frames supplied
Nice to have
• Here is my website as a guide www.tavrento.com.au
Should not have
• Nil

```html
<!DOCTYPE html>
<html lang="en">
<head>
<meta charset="utf-8">
<title>Tavrento – Employer Home</title>
<link rel="stylesheet" href="https://fonts.googleapis.com/css2?family=Inter:wght@300;400;600;700&display=swap">
<style>
  :root {
    --bg: #f9f8fd;
    --ink: #474747;
    --label: #3a3a3a;
    --field-border: #e2ddf6;
    --accent: #8f5cf7;
    --accent-shadow: rgba(143, 92, 247, 0.35);
    --on-accent: #ffffff;
  }
  * { box-sizing: border-box; margin: 0; padding: 0; }
  html, body {
    width: 1200px;
    height: 2597px;
    overflow: hidden;
    background: var(--bg);
    font-family: "Inter", sans-serif;
    color: var(--ink);
  }
  .screen {
    position: relative;
    width: 1200px;
    height: 2597px;
    background: var(--bg);
  }
  .page-title {
    position: absolute;
    left: 151px;
    top: 200px;
    line-height: 1.1;
  }
  .page-title__role {
    display: block;
    font-weight: 300;
    font-size: 100px;
    letter-spacing: 1px;
  }
  .page-title__name {
    display: block;
    font-weight: 700;
    font-size: 70px;
    margin-top: 2px;
  }
  .field {
    position: absolute;
    left: 151px;
    width: 887px;
    height: 168px;
    border: 4px solid var(--field-border);
    border-radius: 28px;
  }
  .field__label {
    position: absolute;
    left: 80px;
    top: -19px;
    padding: 0 14px;
    background: var(--bg);
    font-size: 28px;
    font-weight: 400;
    color: var(--label);
  }
  .field--faded { opacity: 0.45; }
  .fade-out {
    position: absolute;
    left: 0;
    top: 1750px;
    width: 1200px;
    height: 300px;
    background: linear-gradient(to bottom, rgba(249,248,253,0), var(--bg));
  }
  .action {
    position: absolute;
    background: var(--accent);
    color: var(--on-accent);
    border-radius: 24px;
    box-shadow: 0 22px 44px var(--accent-shadow);
    display: flex;
    align-items: center;
    justify-content: center;
    font-weight: 600;
    font-size: 40px;
  }
  .action--scan-workers { left: 377px; top: 2087px; width: 438px; height: 154px; }
  .action--scan-favourites { left: 377px; top: 2328px; width: 438px; height: 154px; }
  .action--tools {
    left: 867px; top: 2087px; width: 171px; height: 397px;
    flex-direction: column;
    justify-content: space-between;
    padding: 48px 0 40px;
  }
  .action--tools svg { display: block; }
</style>
</head>
<body>
<main class="screen">
  <h1 class="page-title">
    <span class="page-title__role">Employer</span>
    <span class="page-title__name">Home</span>
  </h1>

  <div class="field" style="top:481px"><span class="field__label">Venue Name</span></div>
  <div class="field" style="top:704px"><span class="field__label">Contact Person</span></div>
  <div class="field" style="top:928px"><span class="field__label">Email Address</span></div>
  <div class="field" style="top:1148px"><span class="field__label">Mobile Phone</span></div>
  <div class="field" style="top:1365px"><span class="field__label">Location</span></div>
  <div class="field" style="top:1586px"><span class="field__label">Location</span></div>
  <div class="field field--faded" style="top:1806px"><span class="field__label">Location</span></div>
  <div class="fade-out"></div>

  <div class="action action--scan-workers">Scan Workers</div>
  <div class="action action--scan-favourites">Scan Favourite's</div>

  <div class="action action--tools">
    <svg width="110" height="110" viewBox="0 0 110 110" fill="none" stroke="#fff" stroke-width="4" stroke-linecap="round" stroke-linejoin="round" aria-label="Compare">
      <line x1="55" y1="10" x2="55" y2="92"/>
      <circle cx="55" cy="12" r="4"/>
      <line x1="14" y1="24" x2="96" y2="24"/>
      <line x1="36" y1="96" x2="74" y2="96"/>
      <line x1="42" y1="92" x2="68" y2="92"/>
      <path d="M24 24 L10 62 M24 24 L38 62"/>
      <path d="M8 62 H40 A16 12 0 0 1 8 62 Z"/>
      <path d="M86 24 L72 62 M86 24 L100 62"/>
      <path d="M70 62 H102 A16 12 0 0 1 70 62 Z"/>
    </svg>
    <svg width="90" height="90" viewBox="0 0 90 90" fill="none" stroke="#fff" stroke-width="5" stroke-linecap="round" aria-label="Rates">
      <path d="M78 45 A33 33 0 1 1 62 16.5"/>
      <path d="M56 31 C52 26 38 25 36 33 C34 42 56 40 55 52 C54 62 38 62 34 56"/>
      <line x1="45" y1="20" x2="45" y2="26"/>
      <line x1="45" y1="62" x2="45" y2="68"/>
    </svg>
  </div>
</main>
</body>
</html>
```